依頼詳細
今回、既存のリラクゼーションメニューに加えてパーソナルトレーニングのメニューを追加するので新メニューの認知アップの為にチラシを配布する予定です。コロナ渦において外出自粛等で運動不足になっている方や、肩こりや腰痛が少しでも楽になるようにマッサージだけではなく運動も必要とされている方に訴求できるデザインをお願いします。(チラシ持参で初回の45分のトレーニングが半額になります。)
※当店は繁華街によくあるダンベルやバーベルを使った筋力アップを目指すジムとは全くコンセプトが違います。運動不足による筋力低下や年を重ねていくにつれて落ちてくる筋力をカバーしていかに長く健康に生活していけるかをメインにしています。一人でも多くのお客様の日常生活の質を上げることを目的としています。
記載項目
もみほぐし処ことり
www.momihogushi-kotori.jp
06-4821-3390
サイズ
A4
ページ数
片面
希望イメージ
シンプル 複雑
単色 カラフル
暗い 明るい
日常 高級
遊び心 厳粛
未来的 伝統的
女性的 男性的
希望する色
黄・オレンジ系、水色系
納品ファイル
• イラストレーター形式 (.ai)
補足説明

写真や文章の全体のバランスが良く、わかりやすいデザインになっていて好感が持てました。チラシの色合いも統一されていて当店の特徴である暖かさや親しみやすさを感じる内容が良かったです。

今回は当店のチラシデザインを提案していただきありがとうございました。自分では到底このようなデザインを作れることはないので、お願いして本当に助かりました。この度は誠にありがとうございました。

```html
<!DOCTYPE html>
<html lang="ja">
<head>
<meta charset="utf-8">
<title>もみほぐし処ことり トレーニングサービスのご案内</title>
<link rel="stylesheet" href="https://fonts.googleapis.com/css2?family=Noto+Sans+JP:wght@400;500;700;900&family=Roboto:wght@500;700;900&display=swap">
<style>
  :root {
    --yellow: #f6d500;
    --yellow-soft: #fff6b0;
    --red: #e60012;
    --green: #3b9a3f;
    --green-dark: #1f6b23;
    --ink: #1a1a1a;
    --grey: #555;
    --brown: #3a2a20;
    --white: #ffffff;
  }
  * { box-sizing: border-box; margin: 0; padding: 0; }
  html, body { width: 846px; height: 1200px; overflow: hidden; background: var(--white); }
  body { font-family: "Noto Sans JP", sans-serif; color: var(--ink); }
  .flyer { position: relative; width: 846px; height: 1200px; overflow: hidden; }
  .abs { position: absolute; white-space: nowrap; }

  /* header */
  .hero-photo { left: 0; top: 0; width: 846px; height: 328px;
    background: linear-gradient(120deg, #e9e2d6 0%, #cfc6b8 45%, #b9aea0 100%); }
  .brand { left: 18px; top: 6px; display: flex; align-items: center; gap: 8px;
    font-weight: 900; font-size: 28px; line-height: 36px; color: var(--green); }
  .brand-mark { width: 18px; height: 18px; border-radius: 50%; background: var(--green); }
  .title-band { left: 0; width: 846px; text-align: center; font-weight: 900; color: var(--white);
    -webkit-text-stroke: 2px var(--green-dark); paint-order: stroke fill; letter-spacing: 2px; }
  .title-1 { top: 46px; font-size: 58px; background: rgba(59,154,63,.78); height: 80px; line-height: 80px; }
  .title-2 { top: 126px; font-size: 44px; line-height: 56px; }
  .title-3 { top: 182px; font-size: 58px; background: rgba(59,154,63,.78); height: 86px; line-height: 86px; }
  .hero-note { left: 0; top: 286px; width: 846px; text-align: center; font-size: 17px; font-weight: 700;
    color: var(--white); -webkit-text-stroke: 1px var(--green-dark); paint-order: stroke fill; }
  .badge { left: 722px; top: 100px; width: 112px; height: 112px; border-radius: 50%;
    background: var(--yellow); display: flex; align-items: center; justify-content: center;
    text-align: center; font-size: 16px; font-weight: 900; line-height: 1.35; color: var(--ink); }

  /* offer */
  .offer-frame { left: 0; top: 328px; width: 846px; height: 620px; background: var(--yellow); }
  .offer-panel { left: 22px; top: 344px; width: 802px; height: 588px; background: var(--white); }
  .chance-tag { left: 44px; top: 354px; width: 200px; height: 88px; background: var(--ink);
    color: var(--yellow); font-weight: 900; font-size: 32px; text-align: center; line-height: 40px;
    padding-top: 4px; }
  .chance-text { left: 300px; top: 352px; font-size: 27px; font-weight: 900; color: var(--ink);
    line-height: 1.45; padding-left: 18px; border-left: 5px solid var(--red); }
  .price-row { left: 44px; top: 452px; width: 758px; height: 140px; background: var(--yellow-soft); }
  .price-before { left: 66px; top: 466px; font-size: 34px; font-weight: 500; line-height: 1.55; color: var(--grey); }
  .course { left: 330px; top: 454px; font-size: 42px; font-weight: 900; color: var(--red); letter-spacing: 2px; }
  .half { left: 724px; top: 404px; width: 84px; height: 84px; border-radius: 50%; background: var(--red);
    color: var(--white); font-weight: 900; font-size: 28px; display: flex; align-items: center; justify-content: center; }
  .arrow { left: 232px; top: 516px; }
  .price-after { left: 318px; top: 516px; width: 470px; height: 70px; background: var(--yellow);
    text-align: center; font-weight: 900; font-size: 66px;
    line-height: 70px; color: var(--red); letter-spacing: 3px; }
  .price-after small { font-size: 50px; }

  /* contact */
  .contact-lead { left: 60px; top: 604px; font-size: 22px; font-weight: 500; }
  .tel { left: 50px; top: 636px; font-family: "Roboto", sans-serif; font-weight: 900; font-size: 60px; color: var(--red); }
  .tel span { font-size: 40px; }
  .hours-label { left: 60px; top: 728px; font-size: 24px; font-weight: 700; line-height: 1.3; }
  .closed { left: 60px; top: 772px; font-size: 20px; font-weight: 700; color: var(--red); line-height: 1.2; }
  .hours { left: 196px; top: 718px; font-family: "Roboto", sans-serif; font-weight: 900; font-size: 46px; line-height: 56px; }
  .hours small { font-size: 16px; font-weight: 700; margin-left: 6px; }
  .code-box { background: var(--ink); }
  .code-top { left: 596px; top: 604px; width: 210px; height: 222px; }
  .address { left: 520px; top: 838px; width: 290px; font-size: 15px; line-height: 1.45; text-align: right; color: var(--ink); }

  /* massage */
  .massage { left: 0; top: 948px; width: 846px; height: 252px; background: var(--brown); }
  .massage-title { left: 40px; top: 962px; font-size: 24px; font-weight: 700; color: var(--white); }
  .massage-photo { left: 30px; top: 1006px; width: 330px; height: 172px;
    background: linear-gradient(135deg, #a7714a 0%, #d6ab86 55%, #6b4a35 100%); }
  .menu { left: 384px; top: 1010px; color: var(--white); font-size: 16px; line-height: 1.5; }
  .menu dt { font-weight: 700; margin-top: 4px; }
  .menu dd { padding-left: 8px; }
  .info-lead { left: 612px; top: 966px; font-size: 14px; color: var(--white); }
  .code-bottom { left: 612px; top: 992px; width: 200px; height: 190px; }
</style>
</head>
<body>
<main class="flyer">
  <div class="abs hero-photo" role="img" aria-label="トレーナーと利用者が体幹トレーニングをしている写真"></div>
  <div class="abs title-band title-1">トレーニングサービス</div>
  <div class="abs title-band title-2">を</div>
  <div class="abs title-band title-3">はじめました！</div>
  <div class="abs brand"><span class="brand-mark"></span>ことり</div>
  <p class="abs hero-note">新しいメニューでマッサージだけでなく運動も取り入れて健康な毎日を</p>
  <div class="abs badge">初心者のかたに<br>優しいジム</div>

  <div class="abs offer-frame"></div>
  <div class="abs offer-panel"></div>
  <div class="abs chance-tag">今が<br>チャンス</div>
  <p class="abs chance-text">運動不足を感じるあなたへ<br>このチラシを持参で</p>
  <div class="abs price-row"></div>
  <p class="abs price-before">45 分<br>4050 円</p>
  <p class="abs course">体幹トレーニング</p>
  <div class="abs half">半額</div>
  <svg class="abs arrow" width="80" height="56" viewBox="0 0 80 56" aria-hidden="true">
    <polygon points="0,16 46,16 46,0 80,28 46,56 46,40 0,40" fill="#f6d500"/>
  </svg>
  <p class="abs price-after">2000<small>円</small></p>

  <p class="abs contact-lead">お問合せ・お申込みはこちら</p>
  <p class="abs tel"><span>TEL.</span> 06-4821-3390</p>
  <p class="abs hours-label">営業時間</p>
  <p class="abs closed">月曜定休日</p>
  <p class="abs hours">16:00-21:00<small>tue.~fri.</small><br>13:00-21:00<small>sat.・sun</small></p>
  <div class="abs code-box code-top" aria-label="地図"></div>
  <p class="abs address">大阪市城東区新喜多2-4-15<br>ことりビル 2F</p>

  <section class="abs massage"></section>
  <p class="abs massage-title">もみほぐしもご予約受付中！</p>
  <div class="abs massage-photo" role="img" aria-label="もみほぐし施術の写真"></div>
  <dl class="abs menu">
    <dt>もみほぐし</dt>
    <dd>60分 3,180円</dd>
    <dd>75分 3,980円</dd>
    <dd>90分 4,780円</dd>
    <dt>全身もみほぐし</dt>
    <dd>60分 3,980円</dd>
  </dl>
  <p class="abs info-lead">お店の詳しい情報はこちら</p>
  <div class="abs code-box code-bottom" aria-label="店舗情報"></div>
</main>
</body>
</html>
```